Urban Music Nightclub DJ Flyer

The flyer is for a night at a San Diego bar called Copper & Lantern. We tend to play C&L that is more on the bassier side of things but still accessible to the ladies.

The flyer colors would be predominately in black and gold. We're going for a slightly sultry look.

- Ornate Gold frame around the picture.

Changes to the picture:

- Supplied photo has an undesirable tile background
- make it grayscale.

The fonts should complement the frame, have a bit of texture and depth.

Flyer should read

C&L (Largest font)
presents (smallest font)
J TOVAH (Large Font)
BRAXLO x DENHOLM (smaller font)

We've included a quick mock up.

We thank you for the many designs that were submitted. We are close to making our final decision.

```html
<!DOCTYPE html>
<html lang="en">
<head>
<meta charset="utf-8">
<title>C&amp;L presents J Tovah</title>
<link rel="stylesheet" href="https://fonts.googleapis.com/css2?family=Bree+Serif&family=Josefin+Sans:wght@600&display=swap">
<style>
  :root {
    --night: #000000;
    --gold: #f6b922;
    --gold-light: #f9d36a;
    --gold-deep: #9a6410;
    --gold-shadow: #5a3606;
    --rose: #e07d8c;
    --photo-light: #b9b9b9;
    --photo-dark: #4a4a4a;
  }
  html, body {
    margin: 0;
    padding: 0;
    background: var(--night);
    overflow: hidden;
  }
  .flyer {
    position: relative;
    width: 800px;
    height: 1200px;
    background: var(--night);
    overflow: hidden;
  }
  .artwork {
    position: absolute;
    inset: 0;
  }
  .venue-mark {
    position: absolute;
    left: 58px;
    top: -52px;
    margin: 0;
    font-family: "Bree Serif", Georgia, serif;
    font-weight: 400;
    font-size: 318px;
    line-height: 1;
    letter-spacing: 2px;
    color: var(--gold);
  }
  .presents {
    position: absolute;
    left: 79px;
    top: 236px;
    margin: 0;
    font-family: "Josefin Sans", Arial, sans-serif;
    font-weight: 600;
    font-size: 18px;
    color: var(--rose);
  }
  .headliner {
    position: absolute;
    left: 82px;
    top: 272px;
    margin: 0;
    font-family: "Bree Serif", Georgia, serif;
    font-weight: 400;
    font-size: 74px;
    line-height: 1;
    letter-spacing: 2px;
    color: var(--gold);
  }
  .support-acts {
    position: absolute;
    left: 86px;
    top: 360px;
    margin: 0;
    font-family: "Josefin Sans", Arial, sans-serif;
    font-weight: 600;
    font-size: 31px;
    letter-spacing: 1px;
    color: var(--rose);
  }
</style>
</head>
<body>
<main class="flyer">
  <svg class="artwork" width="800" height="1200" viewBox="0 0 800 1200" xmlns="http://www.w3.org/2000/svg">
    <defs>
      <linearGradient id="frame-gold" x1="0" y1="0" x2="1" y2="1">
        <stop offset="0" stop-color="var(--gold-light)"/>
        <stop offset="0.35" stop-color="var(--gold)"/>
        <stop offset="0.7" stop-color="var(--gold-deep)"/>
        <stop offset="1" stop-color="var(--gold)"/>
      </linearGradient>
      <linearGradient id="portrait-tone" x1="0" y1="0" x2="0.4" y2="1">
        <stop offset="0" stop-color="var(--photo-light)"/>
        <stop offset="1" stop-color="var(--photo-dark)"/>
      </linearGradient>
    </defs>

    <g class="gilded-frame" transform="translate(68 518) rotate(-19.5)">
      <rect x="0" y="0" width="592" height="880" fill="url(#frame-gold)"/>
      <rect x="3" y="3" width="586" height="874" fill="none" stroke="var(--gold-shadow)" stroke-width="2"/>
      <rect x="12" y="12" width="568" height="856" fill="none" stroke="var(--gold-shadow)" stroke-width="3" stroke-dasharray="6 5"/>
      <rect x="24" y="24" width="544" height="832" fill="none" stroke="var(--gold-light)" stroke-width="2"/>
      <rect x="36" y="36" width="520" height="808" fill="var(--night)" stroke="var(--gold-shadow)" stroke-width="3"/>
    </g>

    <path class="portrait" role="img" aria-label="Grayscale portrait of the headliner lying back with arms folded above her head, wearing a white tank top"
      d="M176 566 Q230 500 400 478 L588 458 Q640 480 622 566 Q700 700 724 840 L734 1200 L396 1200 L362 880 Q280 800 218 744 Q160 650 176 566 Z"
      fill="url(#portrait-tone)"/>
  </svg>

  <h1 class="venue-mark">C&amp;L</h1>
  <p class="presents">presents</p>
  <h2 class="headliner">J TOVAH</h2>
  <p class="support-acts">BRAXLO &amp; DENHOLM</p>
</main>
</body>
</html>
```